Flyer-Design für Apotheke
Zielgruppe
Wir sind eine Apotheke, mit Schwerpunkt Mutter-Kind / Wiegenhafen Apotheke (www.wiegenhafen Apotheke)
Zielgruppe: Wir haben uns zertifiziert und spezialisiert im Bereich Mütter / Kinderwunsch / Stillen / Babys etc. (Siehe Anbei unser aktueller Entwurf Mutter-Kind-Broschüre)
Wir haben zahlreiche Handouts zu spezifischen Themen von der LHTV und unserem Verein Wiegenhafen Apotheken für unser Kunden schon fertig gestellt (siehe ein Beispiel im Anhang, auf dem wir noch unser Logo eingefügt haben).
Die Handouts sind meist 4-seitig A5, im Anhang mit unserem Logo noch versehen.
Zu zwei Themen möchten wir jetzt noch selbst ein Handout erstellen.
1) Fieberthermometer
2) Schnuller
Ziel: 4-6 Seiten, wir wollen es dann bei Druckfuchs drucken lassen.
Zielgruppe: Mütter, die zu uns in die Apotheke kommen und beraten werden (konkret in diesen Beispielen zum Thema Fieberthermometer bzw. Schnuller. Damit sie was mit nach Hause nehmen können, möchten wir die Handouts erstellen.
Texte anbei, Graphische Umsetzung ggf. mit netten Baby/Mütterbildern o.ä. erwünscht
Aufgabenstellung
Einbau Logo Tolvena-Apotheke (siehe Anhang) ähnlich wie auf dem Flyer Ernährung
(als Logo ohne Adresse etc. und irgendwo unter mit Adresse, Telefon etc.)
Logo Wiegenhafen Apotheke DARF NICHT MIT DRAUF

```html
<!DOCTYPE html>
<html lang="de">
<head>
<meta charset="utf-8">
<title>Der Schnuller – ja oder nein? Informationsbroschüre</title>
<link rel="stylesheet" href="https://fonts.googleapis.com/css2?family=Open+Sans:ital,wght@0,300;0,400;0,600;0,700;1,400&display=swap">
<style>
  :root{
    --backdrop:#5e5e5e;
    --paper:#ffffff;
    --ink:#4a4a4a;
    --ink-soft:#7a7a7a;
    --ink-title:#5a5a5a;
    --box-fill:#e4f1fb;
    --box-line:#9fc7e3;
    --accent:#d6191f;
    --cover-text:#ffffff;
  }
  *{box-sizing:border-box;margin:0;padding:0}
  html,body{width:1200px;height:900px;overflow:hidden}
  body{background:var(--backdrop);font-family:"Open Sans",Arial,sans-serif;color:var(--ink);position:relative}

  .page{position:absolute;top:195px;width:360px;height:509px;background:var(--paper);overflow:hidden;box-shadow:0 6px 18px rgba(0,0,0,.35)}
  .cover{left:40px}
  .spread-left{left:440px;box-shadow:0 6px 18px rgba(0,0,0,.35)}
  .spread-right{left:800px;border-left:1px solid #e2e2e2}

  /* cover */
  .cover-photo{position:absolute;inset:0;
    background:
      radial-gradient(ellipse 38% 55% at 55% 58%, rgba(240,235,230,.55), rgba(240,235,230,0) 70%),
      linear-gradient(180deg,#9c8a3c 0%,#b7a14a 18%,#8e7c3a 34%,#6d4b3c 52%,#7b5445 66%,#c9aaa6 82%,#dcc9c8 100%);}
  .cover-title{position:absolute;top:40px;left:26px;right:20px;color:var(--cover-text);font-weight:300;font-variant:small-caps;font-size:19px;line-height:1.12;letter-spacing:.2px}
  .cover-title small{font-size:13px}
  .cover-sub{position:absolute;top:142px;left:26px;color:var(--cover-text);font-size:11px;font-weight:300}
  .cover-brand{position:absolute;top:12px;right:16px}
  .cover-foot{position:absolute;left:20px;bottom:14px;right:20px;color:var(--cover-text)}
  .cover-foot .brand-name{color:var(--cover-text);font-size:15px}
  .cover-foot .address{font-size:7px;margin-top:2px}
  .cover-foot .web{color:var(--accent);font-weight:700;font-size:12px;margin-top:2px}
  .cover-foot .fine{font-size:4.6px;line-height:1.35;margin-top:3px;opacity:.9}

  .brand{display:flex;align-items:center;gap:4px}
  .brand-name{font-weight:700;font-size:11px;color:#3a3a3a;line-height:1}
  .brand-dot{width:7px;height:7px;border-radius:50%;background:var(--accent)}

  /* inner pages */
  .inner{padding:22px 24px 0 24px;font-size:7.3px;line-height:1.32}
  .inner .brand{position:absolute;top:16px;right:20px}
  .page-title{font-variant:small-caps;font-weight:400;font-size:13px;color:var(--ink-title);margin-top:6px;letter-spacing:.2px}
  .intro{color:var(--ink-soft);margin:5px 0 6px}
  .label{font-style:italic;color:var(--ink-soft);margin:5px 0 3px}
  .section-head{font-size:10px;color:var(--ink-soft);margin:7px 0 4px}
  .infobox{background:var(--box-fill);border:1px solid var(--box-line);padding:5px 8px 6px;list-style:none}
  .infobox li{padding-left:7px;position:relative}
  .infobox li::before{content:"•";position:absolute;left:0}
  .infobox .note{padding-left:0}
  .infobox .note::before{content:none}
  .note b{font-weight:700}
  .closing{color:var(--ink-soft);margin-top:8px;font-size:7.6px;line-height:1.6}
  .page-foot{position:absolute;left:24px;right:24px;bottom:12px;font-size:4.6px;line-height:1.35;color:#666;display:flex;justify-content:space-between;align-items:flex-end;gap:20px}
  .page-no{font-size:5px;white-space:nowrap}
</style>
</head>
<body>

<section class="page cover">
  <div class="cover-photo" role="img" aria-label="Foto: Schwangere Frau im weißen Kleid auf einer Holzbrücke im herbstlichen Wald"></div>
  <div class="cover-brand brand"><span class="brand-name" style="color:var(--cover-text)">Tolvena-Apotheke</span><span class="brand-dot"></span></div>
  <h1 class="cover-title">Der Schnuller – ja oder nein?<br><small>und</small><br>Gewusst, wie! – Fieberthermometer<br>und -messung</h1>
  <p class="cover-sub">Informationsbroschüre</p>
  <div class="cover-foot">
    <div class="brand"><span class="brand-name">Tolvena-Apotheke</span><span class="brand-dot"></span></div>
    <p class="address">Lindenweg 12 · 93101 Falkenried · Tel. 0 12 34 / 56 78 90</p>
    <p class="web">www.tolvena-apotheke.de</p>
    <p class="fine">Die vorliegenden Informationen wurden mit größtmöglicher Sorgfalt zusammengestellt. Layout © Verein Wiegenhafen Apotheke</p>
  </div>
</section>

<section class="page spread-left inner">
  <div class="brand"><span class="brand-name">Tolvena-Apotheke</span><span class="brand-dot"></span></div>
  <h2 class="page-title">Der Schnuller – ja oder nein?</h2>
  <p class="intro">Der Einsatz von Schnullern wird kontrovers diskutiert. Die Entscheidung, ob Sie Ihrem Kind einen Beruhigungssauger geben oder nicht, liegt bei Ihnen.</p>

  <p class="label">Das spricht dafür:</p>
  <ul class="infobox">
    <li>Zur Beruhigung des Säuglings vor allem bei Trennung von Mutter und Kind<br><b>ABER:</b> kein Allheilmittel zur Ruhigstellung</li>
    <li>Schnuller und Daumen als Ersatz für Brust um Saugbedürfnis zu stillen</li>
    <li>Vorteilhafte Auswirkung auf den Saug- und Schluckreflex bei Frühgeborenen</li>
    <li>Protektiver Effekt auf den plötzlichen Kindstod durch regelmäßigen Gebrauch zum Einschlafen</li>
  </ul>

  <p class="label">Das spricht dagegen:</p>
  <ul class="infobox">
    <li>Hungerzeichen des Kindes werden leichter übersehen</li>
    <li>Mögliche verminderte Milchbildung durch zu seltenes Anlegen an der Brust</li>
    <li>Nur Brust passt sich optimal an kindlichen Mund an, auch kiefergerechte Sauger erfüllen Voraussetzungen nicht</li>
    <li>Saugen am Schnuller erfolgt mit anderen Bewegungen als an Brust → mögliche Irritationen beim Trinken</li>
    <li>Zunge liegt nicht in der normalen Ruheposition</li>
    <li>Kann Störungen im Mundraum (Sprechstörungen, Zahn- und Kieferfehlstellungen, etc.) begünstigen</li>
  </ul>

  <p class="intro" style="margin-top:7px">Egal ob Sie sich dafür oder dagegen entscheiden, wichtig ist in jedem Falle ein verantwortungsbewusster und achtsamer Einsatz des Schnullers.</p>

  <h3 class="section-head">Anforderungen an den Schnuller:</h3>
  <ul class="infobox">
    <li>Möglichst niedriger Schnullerschaft → Schneidezähne werden beim Wachstum nicht gehindert</li>
    <li>Raumsparendes und angepasstes Lutschteil → Vermeidung der Entstehung von zu engen oder kleinen Oberkiefern</li>
    <li class="note"><b>Achtung:</b> Kirschsauger verhindern den Mundschluss, daher nicht empfehlenswert.</li>
  </ul>

  <footer class="page-foot">
    <p>Die vorliegenden Informationen wurden mit größtmöglicher Sorgfalt nach dem derzeitigen aktuellen Stand der Wissenschaft zusammengestellt, dennoch übernehmen Verfasser und Herausgeber keine Gewähr. Es besteht kein Anspruch auf Vollständigkeit. Text © Lena Vogt<br>Layout © Verein Wiegenhafen Apotheke</p>
    <span class="page-no">Seite 2</span>
  </footer>
</section>

<section class="page spread-right inner">
  <ul class="infobox" style="margin-top:4px">
    <li>Möglichst flexibles, weiches und bewegliches Lutschteil → mehr Raum für die Zunge als Gaumen- und Kieferformer</li>
    <li class="note"><b>Tipp:</b> Latex ist weicher als Silikon.</li>
    <li>Möglichst leichter Schnuller → Keine Überforderung der Lippen- und Zungenmuskulatur</li>
    <li class="note"><b>Achtung:</b> Schnullerkette erhöht das Gewicht zusätzlich.</li>
    <li>Schnuller muss nicht mitwachsen → Brustwarze verändert sich auch nicht, Zunge braucht wachsenden Freiraum für Sprachentwicklung</li>
    <li>Beruhigungssauger sollte keine Geschmacks- und Zusatzstoffe, sowie gesundheitsschädliche Chemikalien enthalten</li>
  </ul>

  <h3 class="section-head">Wertvolle Tipps beim Umgang mit dem Beruhigungssauger:</h3>
  <ul class="infobox">
    <li>In den ersten 4-6 Wochen möglichst den Gebrauch vermeiden, um die Milchproduktion optimal anlaufen zu lassen</li>
    <li>Schnuller ist kein Ersatz für engen Körperkontakt und Stillen</li>
    <li>Kein Dauergebrauch, nur kurzzeitige Anwendung</li>
    <li>Falls Schnuller beim Schlafen herausfällt, nicht wieder zurück in den Mund schieben</li>
    <li>Schnuller nicht herumliegen lassen, so wird das Kind dazu verleitet</li>
    <li>Sprechen ohne Beruhigungssauger</li>
    <li>Ab dem 2. Lebensjahr mit dem Abgewöhnen beginnen</li>
    <li>Auf hygienischen Umgang achten</li>
  </ul>

  <p class="closing">Bei weiteren Fragen helfen wir Ihnen gerne weiter.<br>Ihr babyfreundliches Team der Tolvena-Apotheke Falkenried</p>

  <footer class="page-foot">
    <p>Die vorliegenden Informationen wurden mit größtmöglicher Sorgfalt nach dem derzeitigen aktuellen Stand der Wissenschaft zusammengestellt, dennoch übernehmen Verfasser und Herausgeber keine Gewähr. Es besteht kein Anspruch auf Vollständigkeit. Text © Lena Vogt<br>Layout © Verein Wiegenhafen Apotheke</p>
    <span class="page-no">Seite 3</span>
  </footer>
</section>

</body>
</html>
```